2-Sided Flyer for Printing - Quarvelent

We are looking for the most attractive and best quality flyer to serve as a handout to distribute as a printed document in fairs and conventions. We want one A4 sheet using two sides to display what is Quarvelent in an attractive and simple way.
• What is Quarvelent, what we do and benefits
o Type of challenges we solve
o Benefit for the companies
o Benefit for the solvers (engineers)
• How does it work
• Sample challenges
• Show our Community (skills, solvers pictures, etc)
The flyer should be developed according to our corporate colours (see landing page and logo)
The material we are uploading is the following:
• Power point with the introduction to Quarvelent
• Sample non professional flyers
• In addition you can use any material available through our web: www.quarvelent-example.com (landing page, blog, clients pages, ranking, etc.)

Target Market(s)

industrial companies and engineers

Industry/Entity Type

Engineering

Requirements
Must have
• A single flyer to be used for companies (clients) and engineers (solvers)
• overall flyer creative design
• clear and clean messages
• contain what is Quarvelent, how it works, community and sample challenges
• social networks info
• corporate pallet
Nice to have
• attractive funnel design to show how to move from a challenge to unique solutions
• attractive way to show the crowd using real solvers pictures
• Not all the background should be coloured (combination of white and corporate colours)
Should not have
• Copy and paste of the provided information and pictures
• High density content
• We do not like the design of the file "Brochure OK final.pdf" and we are looking for a 2-sided flyer

```html
<!DOCTYPE html>
<html lang="en">
<head>
<meta charset="utf-8">
<title>Quarvelent Flyer</title>
<link rel="stylesheet" href="https://fonts.googleapis.com/css2?family=Roboto+Condensed:wght@700&family=Lato:wght@400;700&family=Varela+Round&display=swap">
<style>
  :root {
    --orange: #f15a29;
    --amber: #f7a21b;
    --blue: #27a8e0;
    --ink: #231f20;
    --text: #333333;
    --footer: #231f20;
    --page: #e9e9e9;
    --white: #ffffff;
  }
  * { margin: 0; padding: 0; box-sizing: border-box; }
  html, body { width: 1200px; height: 1200px; overflow: hidden; }
  body { background: var(--page); font-family: 'Lato', sans-serif; color: var(--text); }
  .flyer {
    position: absolute; left: 218px; top: 65px;
    width: 763px; height: 1070px;
    background: var(--white); overflow: hidden;
  }
  .abs { position: absolute; }
  .corner-shapes { left: 0; top: 0; }
  .brand { left: 57px; top: 70px; display: flex; align-items: center; gap: 10px; }
  .brand-dot { width: 22px; height: 22px; border-radius: 50%; background: var(--orange); }
  .brand-name { font-family: 'Varela Round', sans-serif; font-size: 32px; color: #3d3d3d; letter-spacing: 1px; line-height: 1; }
  .rule { left: 0; width: 763px; background: var(--amber); }
  .rule-top { top: 131px; height: 8px; }
  .rule-mid { top: 429px; height: 11px; }
  .community-art {
    left: 77px; top: 180px; width: 616px; height: 234px;
    background: linear-gradient(90deg, #f0643c 0%, #f7a21b 25%, #8cc63f 50%, #27a8e0 75%, #c1272d 100%);
    opacity: .85;
  }
  .headline {
    left: 27px; font-family: 'Roboto Condensed', sans-serif; font-weight: 700;
    line-height: 1; white-space: nowrap; transform-origin: left top;
  }
  .headline-lead { top: 460px; font-size: 68px; color: var(--ink); transform: scaleX(.91); }
  .headline-main { top: 532px; font-size: 62px; color: var(--orange); transform: scaleX(.89); }
  .section-title { font-family: 'Roboto Condensed', sans-serif; font-weight: 700; color: var(--blue); font-size: 20px; line-height: 1; }
  .tagline { left: 29px; top: 614px; }
  .recent-title { left: 26px; top: 768px; }
  .column h3 { font-family: 'Lato', sans-serif; font-weight: 700; font-size: 15px; color: var(--orange); margin-bottom: 3px; }
  .column ul { list-style: none; }
  .column li { font-size: 11.3px; line-height: 13.6px; padding-left: 10px; position: relative; }
  .column li::before { content: ""; position: absolute; left: 0; top: 5px; width: 4px; height: 4px; border-radius: 50%; background: var(--orange); }
  .column-needs { left: 26px; top: 647px; width: 360px; }
  .column-crowd { left: 421px; top: 654px; width: 320px; }
  .challenge { top: 804px; width: 196px; }
  .challenge-photo { width: 196px; height: 144px; border: 3px solid var(--blue); }
  .challenge p { margin-top: 8px; text-align: center; font-size: 12.3px; line-height: 15px; color: var(--ink); }
  .challenge-one { left: 26px; }
  .challenge-one .challenge-photo { background: linear-gradient(160deg, #e4eef3, #9fb4c4 60%, #2d4ea8); }
  .challenge-two { left: 285px; }
  .challenge-two .challenge-photo { background: linear-gradient(160deg, #5d6470, #e3782a 45%, #2f2a28); }
  .challenge-three { left: 542px; }
  .challenge-three .challenge-photo { background: linear-gradient(160deg, #d6d8da, #8f9396 55%, #4d5053); }
  .footer-band { left: 0; top: 1018px; }
  .footer-url { left: 0; top: 1034px; width: 500px; text-align: center; color: var(--white); font-size: 14px; letter-spacing: 3px; }
  .social { left: 551px; top: 1034px; display: flex; gap: 5px; }
  .social span { width: 22px; height: 22px; background: #5a5a5a; border-radius: 2px; }
</style>
</head>
<body>
  <main class="flyer">
    <svg class="abs corner-shapes" width="763" height="640" viewBox="0 0 763 640">
      <polygon points="490,0 763,0 763,139 585,139" fill="var(--orange)"/>
      <polygon points="605,440 763,440 763,630" fill="var(--blue)"/>
    </svg>

    <div class="abs brand">
      <span class="brand-dot"></span>
      <span class="brand-name">quarvelent</span>
    </div>

    <div class="abs rule rule-top"></div>
    <div class="abs community-art" role="img" aria-label="Mosaic of colourful hexagons with engineer avatars and technology icons representing the solver community"></div>
    <div class="abs rule rule-mid"></div>

    <h1 class="abs headline headline-lead">The Hub for</h1>
    <h2 class="abs headline headline-main">ENGINEERING INNOVATION</h2>
    <p class="abs section-title tagline">ENGINEERING INNOVATION THROUGH THE CROWD</p>

    <section class="abs column column-needs">
      <h3>Companies’ needs</h3>
      <ul>
        <li>Be more competitive through product and process innovation</li>
        <li>Deliver better innovation results through better solutions</li>
        <li>Reduce uncertainties when adopting new technologies</li>
        <li>Increase capacity of internal engineering teams</li>
      </ul>
    </section>

    <section class="abs column column-crowd">
      <h3>The Crowd Engineering ‘Opportunity’</h3>
      <ul>
        <li>Connect with broader talent and experience from a global and diverse engineering community</li>
        <li>Bring innovations from other industries</li>
        <li>Enhance internal innovation culture looking outside</li>
        <li>Extend the supplier network with a broader perspective</li>
      </ul>
    </section>

    <h3 class="abs section-title recent-title">RECENT CHALLENGES</h3>

    <figure class="abs challenge challenge-one">
      <div class="challenge-photo" role="img" aria-label="Plastic water bottles with blue caps"></div>
      <p>Eco Friendly Packaging Design<br>Challenge (8K in Prizes)</p>
    </figure>
    <figure class="abs challenge challenge-two">
      <div class="challenge-photo" role="img" aria-label="Foundry worker pouring molten metal in a factory"></div>
      <p>Automatic Alignment System<br>Project (10 K € in Prizes)</p>
    </figure>
    <figure class="abs challenge challenge-three">
      <div class="challenge-photo" role="img" aria-label="Stacked bundles of steel tubes with tags"></div>
      <p>The Productivity Project for Tubes<br>Packing (8-12K € in Prizes)</p>
    </figure>

    <svg class="abs footer-band" width="763" height="52" viewBox="0 0 763 52">
      <polygon points="0,0 498,0 450,52 0,52" fill="var(--footer)"/>
    </svg>
    <p class="abs footer-url">www.quarvelent-example.com</p>
    <div class="abs social" aria-label="Social network links">
      <span></span><span></span><span></span><span></span><span></span><span></span>
    </div>
  </main>
</body>
</html>
```